JMT - Business Card Design Project

We need a business card based on our logo
Updates

Hi I just upload logo file in AI format Thanks and regards

Target Market(s)

Bank, Big companies, Business owners

Industry/Entity Type

Business

Font styles to use
Sans Serif

```html
<!DOCTYPE html>
<html lang="fr">
<head>
<meta charset="utf-8">
<title>JMT – Carte de visite</title>
<link rel="stylesheet" href="https://fonts.googleapis.com/css2?family=Open+Sans:wght@300;400;600&display=swap">
<style>
  :root {
    --backdrop: #7f9194;
    --card-black: #050505;
    --card-sheen: #2b2b2b;
    --ink-white: #f4f4f4;
    --ink-soft: #cfd3d6;
    --band-blue: #22395d;
    --accent-blue: #3d5d8c;
  }
  * { margin: 0; padding: 0; box-sizing: border-box; }
  html, body {
    width: 1200px; height: 900px; overflow: hidden;
    background: var(--backdrop);
    font-family: "Open Sans", Arial, sans-serif;
  }
  .stage {
    width: 1200px; height: 900px;
    display: flex; align-items: center; justify-content: center;
  }
  .business-card {
    position: relative;
    width: 840px; height: 480px;
    background:
      radial-gradient(ellipse 55% 70% at 30% 60%, var(--card-sheen) 0%, rgba(43,43,43,0) 70%),
      var(--card-black);
    color: var(--ink-white);
    overflow: hidden;
  }
  .divider-line {
    position: absolute; left: 320px; top: 244px;
    width: 260px; height: 2px;
    background: linear-gradient(90deg, rgba(61,93,140,0) 0%, var(--accent-blue) 50%, rgba(61,93,140,0) 100%);
  }
  .contact-block {
    position: absolute; left: 520px; top: 70px;
  }
  .person-name {
    font-weight: 600; font-size: 26px; letter-spacing: 0.5px;
    text-transform: uppercase;
  }
  .person-title {
    font-weight: 400; font-size: 20px; color: var(--ink-soft);
    margin: 2px 0 26px 40px;
  }
  .contact-list { list-style: none; }
  .contact-item {
    display: flex; align-items: center; gap: 10px;
    font-size: 19px; font-weight: 400; margin-bottom: 6px;
    padding-left: 70px;
  }
  .contact-item svg { width: 14px; height: 14px; fill: var(--ink-soft); flex: none; }
  .brand-block {
    position: absolute; left: 90px; bottom: 130px;
    display: flex; align-items: flex-end; gap: 24px;
  }
  .brand-name {
    display: flex; align-items: center; gap: 12px;
    font-weight: 600; font-size: 60px; line-height: 1;
    color: var(--ink-white);
  }
  .brand-square {
    width: 18px; height: 18px; background: var(--accent-blue);
  }
  .firm-name {
    font-weight: 400; font-size: 22px; color: var(--ink-soft);
    padding-bottom: 4px;
  }
  .service-band {
    position: absolute; left: 320px; right: 0; bottom: 70px;
    height: 44px; background: var(--band-blue);
    display: flex; align-items: center; padding-left: 30px;
    font-size: 22px; font-weight: 400; color: var(--ink-white);
    letter-spacing: 0.3px;
  }
</style>
</head>
<body>
  <main class="stage">
    <section class="business-card" aria-label="Carte de visite JMT">
      <div class="divider-line"></div>

      <div class="contact-block">
        <p class="person-name">Paul Durand</p>
        <p class="person-title">Director</p>
        <ul class="contact-list">
          <li class="contact-item">
            <svg viewBox="0 0 16 16" aria-hidden="true"><path d="M3.5 1l2.5 3-1.6 1.6a9 9 0 0 0 5.5 5.5L11.5 9.5l3 2.5-1.5 2.5C7 15 1 9 1 2.5z"/></svg>
            <span>+123 555 0142</span>
          </li>
          <li class="contact-item">
            <svg viewBox="0 0 16 16" aria-hidden="true"><path d="M1 3h14v10H1z M1.8 3.8L8 9l6.2-5.2" stroke="#050505" stroke-width="1.2"/></svg>
            <span>pauldurand@mail.com</span>
          </li>
          <li class="contact-item">
            <svg viewBox="0 0 16 16" aria-hidden="true"><path d="M8 1a5 5 0 0 1 5 5c0 4-5 9-5 9S3 10 3 6a5 5 0 0 1 5-5zm0 3a2 2 0 1 0 0 4 2 2 0 0 0 0-4z"/></svg>
            <span>www.jmt.com</span>
          </li>
        </ul>
      </div>

      <div class="brand-block">
        <p class="brand-name"><span class="brand-square" aria-hidden="true"></span>JMT</p>
        <p class="firm-name">Cabinet Jolivet Marchand &amp; Associés</p>
      </div>

      <div class="service-band">Expertise-comptable · Audit · Conseil</div>
    </section>
  </main>
</body>
</html>
```